The amber lantern with an elephant incorporated in the background

Target Market(s)

Real estate

Industry/Entity Type

Real Estate

Contact Information for Business Card

On back on want my name & number
In front I want the business name, "the amber lantern", below to say staging & design

Logo Text

The amber lantern

Font styles to use
Serif

Colors
000000

Requirements
Must have
• I want an elephant behind the writing in gold transperant

```html
<!DOCTYPE html>
<html lang="en">
<head>
<meta charset="utf-8">
<title>The Amber Lantern – Business Cards</title>
<link href="https://fonts.googleapis.com/css2?family=Libre+Baskerville:wght@400;700&display=swap" rel="stylesheet">
<style>
  :root {
    --backdrop: #2b2b2b;
    --card-black: #080808;
    --pattern-tone: #1c1c1c;
    --gold: #f4a93a;
    --gold-line: #b9812c;
    --gold-ghost: rgba(244,169,58,.16);
    --elephant-brown: #6e5837;
    --amber-band: #f8ad3c;
    --white: #f2f2f2;
  }
  * { box-sizing: border-box; margin: 0; padding: 0; }
  html, body {
    width: 1200px; height: 1200px; overflow: hidden;
    background: var(--backdrop);
    font-family: "Libre Baskerville", Georgia, serif;
  }
  .sheet {
    width: 1200px; height: 1200px;
    display: flex; flex-direction: column; align-items: center; justify-content: center;
    gap: 60px;
  }
  .card {
    position: relative;
    width: 840px; height: 480px;
    background: var(--card-black);
    overflow: hidden;
    box-shadow: 0 10px 30px rgba(0,0,0,.45);
  }
  .card__pattern {
    position: absolute; inset: 0;
    background:
      radial-gradient(ellipse at 25% 35%, var(--pattern-tone) 0%, transparent 45%),
      radial-gradient(ellipse at 75% 60%, var(--pattern-tone) 0%, transparent 50%),
      radial-gradient(ellipse at 50% 90%, #151515 0%, transparent 40%);
  }
  .elephant-watermark {
    position: absolute; left: 50%; transform: translateX(-50%);
    width: 380px; height: 260px; border-radius: 50%;
    background: radial-gradient(ellipse at center, var(--gold-ghost) 0%, rgba(244,169,58,.07) 55%, transparent 75%);
  }
  .card--front .elephant-watermark { top: 110px; }
  .card--back .elephant-watermark { top: 40px; }
  .brand {
    position: absolute; left: 0; right: 0;
    display: flex; flex-direction: column; align-items: center;
  }
  .card--front .brand { top: 170px; }
  .card--back .brand { top: 92px; }
  .brand__name {
    color: var(--gold);
    font-size: 48px; font-weight: 400; letter-spacing: .5px;
    line-height: 1.1;
  }
  .brand__rule {
    display: flex; align-items: center; gap: 10px;
    width: 580px; margin-top: 10px;
  }
  .brand__line { height: 1px; background: var(--gold-line); }
  .brand__line--long { flex: 1; }
  .brand__line--short { width: 70px; }
  .brand__tagline {
    color: var(--gold);
    font-size: 20px; letter-spacing: 1px; font-style: normal;
  }
  .contact {
    position: absolute; top: 215px; left: 0; right: 0;
    text-align: center;
  }
  .contact__name {
    color: var(--gold);
    font-size: 32px; font-weight: 700; letter-spacing: 1px;
  }
  .contact__phone {
    color: var(--white);
    font-size: 20px; margin-top: 10px;
  }
  .elephant-parade {
    position: absolute; left: 0; right: 0; bottom: 20px; height: 90px;
    background: linear-gradient(90deg, rgba(110,88,55,.25), rgba(110,88,55,.75) 50%, rgba(110,88,55,.25));
  }
  .amber-band {
    position: absolute; left: 0; right: 0; bottom: 0; height: 20px;
    background: var(--amber-band);
  }
</style>
</head>
<body>
<main class="sheet">
  <section class="card card--front">
    <div class="card__pattern" role="img" aria-label="Faint dark floral scroll pattern"></div>
    <div class="elephant-watermark" role="img" aria-label="Transparent gold elephant behind the business name"></div>
    <div class="brand">
      <h1 class="brand__name">The Amber Lantern</h1>
      <div class="brand__rule">
        <span class="brand__line brand__line--long"></span>
        <span class="brand__tagline">staging &amp; design</span>
        <span class="brand__line brand__line--short"></span>
      </div>
    </div>
  </section>

  <section class="card card--back">
    <div class="card__pattern" role="img" aria-label="Faint dark floral scroll pattern"></div>
    <div class="elephant-watermark" role="img" aria-label="Transparent gold elephant behind the business name"></div>
    <div class="brand">
      <h2 class="brand__name">The Amber Lantern</h2>
      <div class="brand__rule">
        <span class="brand__line brand__line--long"></span>
        <span class="brand__tagline">staging &amp; design</span>
        <span class="brand__line brand__line--short"></span>
      </div>
    </div>
    <div class="contact">
      <p class="contact__name">JANE MARLOW</p>
      <p class="contact__phone">1-555-201-4486</p>
    </div>
    <div class="elephant-parade" role="img" aria-label="Row of small bronze elephants walking trunk to tail"></div>
    <div class="amber-band"></div>
  </section>
</main>
</body>
</html>
```